Hi everyone,
Bright Nest Homes is a business that renovates older houses into modern homes. I'm looking for a design that is clean and simple. It needs to show the client that renovating is a simple process. No more than 3 colours to be used thanks.

What I need:
1. Logo
2. Business card (one side)
3. Letter head (A4)

Looking forward to the designs!

Industry/Entity Type

Construction

Logo Text

Bright Nest Homes

Font styles to use
Sans Serif

Requirements
Must have
• Trading name: Bright Nest Homes
• Contact name: Declan Ferris
• Email: declanferris@brightnesthomes.com.au
• Tel: 0417 582 046
• Clean and simple
Nice to have
• If design might include a few tools. eg Hammer, paint roller etc.
Should not have
• Complicated design

```html
<!DOCTYPE html>
<html lang="en">
<head>
<meta charset="utf-8">
<title>Bright Nest Homes — Stationery</title>
<link rel="stylesheet" href="https://fonts.googleapis.com/css2?family=Open+Sans:ital,wght@0,400;0,700;1,400&display=swap">
<style>
  :root {
    --bg: #f1f1f1;
    --paper: #ffffff;
    --ink: #1e1e1e;
    --muted: #6b6b6b;
    --green: #14a04a;
    --plan: #f3f3f3;
    --plan-edge: #ebebeb;
  }
  * { box-sizing: border-box; margin: 0; padding: 0; }
  html, body {
    width: 1200px; height: 726px; overflow: hidden;
    background: var(--bg);
    font-family: "Open Sans", sans-serif;
    color: var(--ink);
  }
  .stage { position: relative; width: 1200px; height: 726px; }

  .letterhead {
    position: absolute; left: 70px; top: 50px;
    width: 440px; height: 622px;
    background: var(--paper);
    box-shadow: 0 6px 18px rgba(0,0,0,.12);
    overflow: hidden;
  }
  .letterhead .plan-backdrop {
    position: absolute; left: 0; top: 60px; right: 0; bottom: 40px;
    background: radial-gradient(ellipse at 60% 40%, var(--plan) 0%, var(--paper) 75%);
  }
  .letterhead .brand {
    position: absolute; right: 30px; top: 28px;
    font-size: 20px; font-weight: 700; letter-spacing: -.2px;
  }
  .letterhead .tools-art {
    position: absolute; right: 40px; bottom: 36px;
    width: 110px; height: 100px;
    background: linear-gradient(135deg, #f4f4f4, #e2ece5);
    clip-path: polygon(25% 0, 75% 0, 100% 50%, 75% 100%, 25% 100%, 0 50%);
  }
  .letterhead .footer-contact {
    position: absolute; left: 22px; bottom: 32px;
    display: flex; gap: 10px; align-items: center;
    font-size: 7.5px; color: var(--muted); font-style: italic;
  }
  .letterhead .footer-contact span { display: inline-flex; align-items: center; gap: 3px; }
  .letterhead .band {
    position: absolute; left: 0; right: 0; bottom: 16px; height: 8px;
    background: var(--green);
  }

  .business-card {
    position: absolute; left: 600px; top: 214px;
    width: 540px; height: 300px;
    background: var(--paper);
    box-shadow: 0 6px 18px rgba(0,0,0,.12);
    overflow: hidden;
  }
  .business-card .plan-backdrop {
    position: absolute; inset: 0 0 46px 0;
    background: radial-gradient(ellipse at 50% 45%, var(--paper) 25%, var(--plan) 80%);
  }
  .business-card .brand {
    position: absolute; left: 0; right: 0; top: 98px;
    text-align: center;
    font-size: 40px; font-weight: 700; letter-spacing: -.5px;
  }
  .business-card .person {
    position: absolute; left: 0; right: 0; top: 164px;
    text-align: center;
    font-size: 19px; font-style: italic; color: var(--green);
  }
  .business-card .contact-row {
    position: absolute; left: 0; right: 0; top: 226px;
    display: flex; justify-content: center; gap: 26px;
    font-size: 14px; font-style: italic; color: var(--muted);
  }
  .business-card .contact-row span { display: inline-flex; align-items: center; gap: 7px; }
  .business-card .band {
    position: absolute; left: 0; right: 0; bottom: 22px; height: 11px;
    background: var(--green);
  }
  .icon { flex: none; }
</style>
</head>
<body>
<main class="stage">

  <section class="letterhead" aria-label="Letterhead">
    <div class="plan-backdrop" role="img" aria-label="Faint architectural floor plan drawing"></div>
    <div class="brand">Bright Nest Homes</div>
    <div class="tools-art" role="img" aria-label="Paint roller, hammer and spanner in hexagon frames"></div>
    <div class="footer-contact">
      <span>Example Example Example Example Example Example</span>
      <span>
        <svg class="icon" width="9" height="9" viewBox="0 0 20 20"><circle cx="10" cy="10" r="9" fill="none" stroke="#6b6b6b" stroke-width="1.5"/><path d="M7 5c-1 1-1 3 1 6s4 4 5 4l1-2-2-1-1 1c-1 0-3-2-3-3l1-1-1-2z" fill="#6b6b6b"/></svg>
        0417 582 046
      </span>
      <span>
        <svg class="icon" width="9" height="9" viewBox="0 0 20 20"><circle cx="10" cy="10" r="9" fill="none" stroke="#6b6b6b" stroke-width="1.5"/><rect x="5" y="7" width="10" height="7" fill="none" stroke="#6b6b6b" stroke-width="1.2"/><path d="M5 7l5 4 5-4" fill="none" stroke="#6b6b6b" stroke-width="1.2"/></svg>
        declanferris@brightnesthomes.com.au
      </span>
    </div>
    <div class="band"></div>
  </section>

  <section class="business-card" aria-label="Business card">
    <div class="plan-backdrop" role="img" aria-label="Faint architectural floor plan drawing"></div>
    <div class="brand">Bright Nest Homes</div>
    <div class="person">Declan Ferris</div>
    <div class="contact-row">
      <span>
        <svg class="icon" width="17" height="17" viewBox="0 0 20 20"><circle cx="10" cy="10" r="9" fill="none" stroke="#6b6b6b" stroke-width="1.4"/><path d="M7 5c-1 1-1 3 1 6s4 4 5 4l1-2-2-1-1 1c-1 0-3-2-3-3l1-1-1-2z" fill="#6b6b6b"/></svg>
        0417 582 046
      </span>
      <span>
        <svg class="icon" width="17" height="17" viewBox="0 0 20 20"><circle cx="10" cy="10" r="9" fill="none" stroke="#6b6b6b" stroke-width="1.4"/><rect x="5" y="7" width="10" height="7" fill="none" stroke="#6b6b6b" stroke-width="1.2"/><path d="M5 7l5 4 5-4" fill="none" stroke="#6b6b6b" stroke-width="1.2"/></svg>
        declanferris@brightnesthomes.com.au
      </span>
    </div>
    <div class="band"></div>
  </section>

</main>
</body>
</html>
```